Varneck Bidding Business Cards Design Needed

I need a business card design that is modern looking - double sided (maybe just my logo on the back, but open to suggestions) - the overall design is up to you. I want it to be easy to read - not over the top flashy. I already have a company logo which I uploaded so that needs to be used. The colors of my logo are the colors I want on the card... so blue and gray (do need to match the logo colors).

Requirements
Must have
• Would like the card to be sleek, modern and easy to ready

```html
<!DOCTYPE html>
<html lang="en">
<head>
<meta charset="utf-8">
<title>Varneck Bidding – Business Cards</title>
<link rel="stylesheet" href="https://fonts.googleapis.com/css2?family=Cabin:wght@400;600;700&display=swap">
<style>
  :root {
    --backdrop: #e01d1d;
    --brand-blue: #0678b4;
    --brand-gray: #58595b;
    --paper: #f2f2f2;
    --soft-text: #d8d8d8;
  }
  html, body {
    margin: 0;
    padding: 0;
    width: 1200px;
    height: 1200px;
    overflow: hidden;
    background: var(--backdrop);
    font-family: "Cabin", "Segoe UI", sans-serif;
  }
  .canvas {
    position: relative;
    width: 1200px;
    height: 1200px;
  }
  .card {
    position: absolute;
    display: block;
  }
  .card--front { left: 173px; top: 83px; width: 798px; height: 443px; }
  .card--back  { left: 172px; top: 654px; width: 796px; height: 442px; }
  .fill-blue { fill: var(--brand-blue); }
  .fill-gray { fill: var(--brand-gray); }
  .fill-paper { fill: var(--paper); }
  .edge { stroke: var(--paper); stroke-width: 5; stroke-linejoin: round; }
  .company { font-weight: 700; font-size: 62px; fill: var(--brand-blue); }
  .person { font-weight: 700; font-size: 40px; fill: var(--brand-blue); }
  .detail { font-weight: 600; font-size: 42px; fill: var(--soft-text); text-anchor: end; }
  .website { font-weight: 400; font-size: 38px; fill: var(--soft-text); }
  .brand-name { font-weight: 700; font-size: 64px; fill: var(--brand-blue); text-anchor: middle; }
</style>
</head>
<body>
<main class="canvas">

  <!-- Front of card -->
  <svg class="card card--front" viewBox="0 0 998 554" aria-label="Business card front">
    <rect class="fill-paper" width="998" height="554"/>
    <rect class="fill-gray" x="0" y="0" width="54" height="554"/>
    <path class="fill-gray" d="M630 0 L690 78 Q712 102 760 102 L998 102 L998 0 Z"/>
    <path class="fill-blue" d="M74 406 L280 178 Q340 108 450 108 L998 108 L998 406 Z"/>
    <path class="fill-gray" d="M74 412 L240 554 L852 554 L742 458 Q700 412 620 412 Z"/>

    <text class="website" transform="translate(14 28) rotate(90)">http://bidrecovery.com</text>

    <text class="company" x="84" y="76">Varneck Bidding, Inc.</text>
    <text class="person" x="88" y="124">Marla Quinlan</text>

    <text class="detail" x="970" y="183">Owner/President - Auctioneer</text>
    <text class="detail" x="966" y="256">Phone: 702-555-0148</text>
    <text class="detail" x="966" y="314">email: varneckbid@mailpost.com</text>
    <text class="detail" x="970" y="372">Improving Charity Auctions Nationwide</text>
  </svg>

  <!-- Back of card -->
  <svg class="card card--back" viewBox="0 0 995 553" aria-label="Business card back">
    <rect class="fill-gray" width="995" height="553"/>
    <path class="fill-paper edge" d="M315 0 L685 0 L912 182 L790 315 Q755 375 690 375 L495 375 L680 553 L310 553 L85 373 L190 240 Q240 178 300 178 L505 178 Z"/>

    <g class="stripes">
      <path class="fill-blue" d="M330 2 L682 2 L905 180 Z"/>
      <path class="fill-gray edge" d="M332 4 L384 60 L903 182 Z"/>
      <path class="fill-blue" d="M388 64 L902 186 L855 238 Z"/>
    </g>
    <g class="stripes" transform="rotate(180 497 277)">
      <path class="fill-blue" d="M330 2 L682 2 L905 180 Z"/>
      <path class="fill-gray edge" d="M332 4 L384 60 L903 182 Z"/>
      <path class="fill-blue" d="M388 64 L902 186 L855 238 Z"/>
    </g>

    <text class="brand-name" x="500" y="298">Varneck Bidding</text>
  </svg>

</main>
</body>
</html>
```